Professional Home Buyer business card needed

I need a pretty straight forward business card designed. We help people that NEED to sell their homes solve problems. We perform all types of Real Estate transactions including flip, wholesale, investment, rental property and multi family. The card will mainly be used to give to prospective Sellers but will also be given to Real Estate Investors as well. It should professional and very easy to read, most clients are older people.

Target Market(s)

Distressed home sellers as well as Real Estate investors

Industry/Entity Type

Real Estate

Contact Information for Business Card

should be a professional layout

Colors
ec1f27
ffffff
000000

Requirements
Must have
• Large logo on back and smaller one on front. should utilize Red, white, and black.
• I am thinking of using a soft touch coating on the card so keep that in mind.
• Contact info should be very easy to read, think older clients.
Nice to have
• I would like to see a design with rounded corners on the card
Should not have
• pictures of homes or other home graphics.

```html
<!DOCTYPE html>
<html lang="en">
<head>
<meta charset="utf-8">
<title>Summit Home Buyers – Business Card</title>
<link rel="stylesheet" href="https://fonts.googleapis.com/css2?family=Arimo:wght@400;700&family=Oswald:wght@500;600&display=swap">
<style>
  :root {
    --brand-red: #ec1f27;
    --ink: #000000;
    --paper: #ffffff;
    --stage: #e9e9ea;
    --muted: #cfcfcf;
    --body-font: "Arimo", Arial, sans-serif;
    --head-font: "Oswald", "Arial Narrow", sans-serif;
  }
  * { box-sizing: border-box; margin: 0; padding: 0; }
  html, body { width: 1200px; height: 1000px; overflow: hidden; }
  body {
    background: var(--stage);
    font-family: var(--body-font);
    color: var(--ink);
    display: flex;
    align-items: center;
    justify-content: center;
    gap: 40px;
  }
  .card {
    position: relative;
    width: 540px;
    height: 309px;
    background: var(--paper);
    border-radius: 22px;
    overflow: hidden;
    box-shadow: 0 6px 18px rgba(0,0,0,0.18);
  }

  /* Back card: services */
  .card-back .brand-mark {
    position: absolute;
    left: 28px; top: 30px;
    display: flex; align-items: center; gap: 10px;
  }
  .brand-square { width: 22px; height: 22px; background: var(--brand-red); }
  .brand-name {
    font-family: var(--body-font);
    font-weight: 700;
    font-size: 22px;
    line-height: 1.05;
    text-transform: uppercase;
    color: var(--ink);
  }
  .card-back .company-heading {
    position: absolute;
    right: 26px; top: 30px;
    font-family: var(--head-font);
    font-weight: 600;
    font-size: 30px;
    letter-spacing: 0.5px;
  }
  .card-back .services-intro {
    position: absolute;
    left: 180px; top: 118px;
    color: var(--brand-red);
    font-weight: 700;
    font-size: 25px;
  }
  .services-list {
    position: absolute;
    left: 180px; top: 160px;
    list-style: none;
  }
  .services-list li {
    position: relative;
    padding-left: 28px;
    font-weight: 700;
    font-size: 18px;
    line-height: 1.15;
    margin-bottom: 8px;
  }
  .services-list li svg {
    position: absolute; left: 0; top: 2px;
  }

  /* Front card: contact */
  .card-front .side-panel {
    position: absolute; inset: 0;
  }
  .card-front .panel-brand {
    position: absolute;
    left: 24px; top: 26px;
    display: flex; align-items: center; gap: 8px;
  }
  .card-front .panel-brand .brand-name { color: var(--paper); font-size: 17px; }
  .card-front .panel-brand .brand-square { width: 16px; height: 16px; }
  .address {
    position: absolute;
    left: 34px; top: 140px;
    color: var(--paper);
    font-size: 16px;
    line-height: 1.35;
  }
  .address svg { display: block; margin-bottom: 10px; }
  .faint-brand {
    position: absolute;
    left: 262px; top: 118px;
    font-weight: 700;
    font-size: 22px;
    color: var(--muted);
    text-transform: uppercase;
  }
  .person {
    position: absolute;
    right: 28px; top: 40px;
    text-align: right;
  }
  .person-name { font-weight: 700; font-size: 32px; }
  .person-title { font-weight: 700; font-size: 21px; margin-top: 2px; }
  .contact {
    position: absolute;
    right: 28px; bottom: 28px;
    text-align: right;
    font-size: 17px;
    line-height: 1.4;
  }
  .contact .phone { font-weight: 700; font-size: 19px; margin-bottom: 4px; }
</style>
</head>
<body>

  <section class="card card-back" aria-label="Business card back">
    <div class="brand-mark">
      <span class="brand-square"></span>
      <span class="brand-name">Summit<br>Home Buyers</span>
    </div>
    <h1 class="company-heading">SUMMIT HOME BUYERS</h1>
    <p class="services-intro">We perform all types of</p>
    <ul class="services-list">
      <li><svg width="18" height="16" viewBox="0 0 18 16"><path d="M0 0 L18 0 L9 16 Z" fill="var(--brand-red)"/></svg>Real Estate transactions including flip</li>
      <li><svg width="18" height="16" viewBox="0 0 18 16"><path d="M0 0 L18 0 L9 16 Z" fill="var(--brand-red)"/></svg>Wholesale, Investment</li>
      <li><svg width="18" height="16" viewBox="0 0 18 16"><path d="M0 0 L18 0 L9 16 Z" fill="var(--brand-red)"/></svg>Rental property and multi family</li>
    </ul>
  </section>

  <section class="card card-front" aria-label="Business card front">
    <svg class="side-panel" width="540" height="309" viewBox="0 0 540 309">
      <path d="M0 0 H250 C180 90 175 220 215 309 H0 Z" fill="var(--ink)"/>
    </svg>
    <div class="panel-brand">
      <span class="brand-square"></span>
      <span class="brand-name">Summit<br>Home Buyers</span>
    </div>
    <div class="address">
      <svg width="20" height="28" viewBox="0 0 20 28"><path d="M10 0 C4.5 0 0 4.5 0 10 C0 17 10 28 10 28 C10 28 20 17 20 10 C20 4.5 15.5 0 10 0 Z" fill="var(--brand-red)"/><circle cx="10" cy="10" r="4" fill="var(--ink)"/></svg>
      P.O. Box 112<br>Milltown<br>KS 67000
    </div>
    <p class="faint-brand">Summit Home Buyers</p>
    <div class="person">
      <p class="person-name">Daniel Mercer</p>
      <p class="person-title">President</p>
    </div>
    <div class="contact">
      <p class="phone">316-555-0148</p>
      <p>dan@plainshomesforcash.com</p>
      <p>www.plainshomesforcash.com</p>
    </div>
  </section>

</body>
</html>
```